Communications & Broadcast Consulting/PR/Media Relations & Public Affairs

My main goals are to provide communications support to school districts, small towns/cities/hospitals and private businesses in the form of press releases, media relations, public affairs. I also have 25 years experience as a television news anchor/reporter and I'm open to free-lance reporting in both Indianapolis and other markets. My specialty is working with the media.
Communications

```html
<!DOCTYPE html>
<html lang="en">
<head>
<meta charset="utf-8">
<title>Whitmore Communications – Business Card</title>
<link rel="stylesheet" href="https://fonts.googleapis.com/css2?family=Josefin+Sans:wght@400;600&family=Oswald:wght@400&display=swap">
<style>
  :root {
    --page-bg: #eceeed;
    --silver-edge: #b9bbbe;
    --silver-mid: #e4e5e7;
    --silver-light: #ffffff;
    --brand-blue: #1f5ea8;
    --deep-blue: #1b3f86;
    --bright-blue: #2d93d2;
    --ink: #2f2f33;
    --white: #ffffff;
  }
  * { margin: 0; padding: 0; box-sizing: border-box; }
  html, body {
    width: 853px; height: 1200px; overflow: hidden;
    background: var(--page-bg);
  }
  .card {
    position: absolute; left: 96px; top: 48px;
    width: 660px; height: 1104px; overflow: hidden;
    background: linear-gradient(90deg, var(--silver-edge) 0%, var(--silver-mid) 22%, var(--silver-light) 50%, var(--silver-mid) 78%, var(--silver-edge) 100%);
    font-family: "Josefin Sans", "Century Gothic", sans-serif;
    color: var(--ink);
  }
  .person-name {
    position: absolute; top: 64px; left: 0; width: 100%;
    text-align: center; font-size: 38px; font-weight: 600;
    font-variant: small-caps; letter-spacing: 2px; color: var(--brand-blue);
  }
  .person-role {
    position: absolute; top: 112px; left: 0; width: 100%;
    text-align: center; font-size: 29px; font-weight: 600;
    font-variant: small-caps; letter-spacing: 1.5px;
  }
  .contact-line {
    position: absolute; display: flex; align-items: center; gap: 6px;
    font-size: 30px; font-weight: 600; letter-spacing: 3px; white-space: nowrap;
  }
  .contact-line svg { flex: none; }
  .line-phone { top: 172px; left: 170px; }
  .line-mobile { top: 222px; left: 170px; }
  .line-email { top: 274px; left: 70px; font-size: 28px; letter-spacing: 1.5px; font-variant: small-caps; }
  .line-address { top: 334px; left: 40px; font-size: 28px; letter-spacing: 1.5px; font-variant: small-caps; }
  .address-city {
    position: absolute; top: 378px; left: 280px;
    font-size: 28px; font-weight: 600; letter-spacing: 1.5px; font-variant: small-caps;
  }
  .brand-mark-area {
    position: absolute; left: 190px; top: 460px; width: 280px; height: 440px;
    background: radial-gradient(ellipse at 50% 55%, rgba(45,147,210,0.28) 0%, rgba(31,94,168,0.12) 45%, rgba(255,255,255,0) 72%);
  }
  .footer-band { position: absolute; left: 0; bottom: 0; width: 660px; height: 240px; }
  .company-name {
    position: absolute; left: 0; bottom: 56px; width: 100%;
    text-align: center; font-family: "Oswald", "Arial Narrow", sans-serif;
    font-size: 60px; font-weight: 400; font-variant: small-caps;
    letter-spacing: 1px; color: var(--white);
  }
</style>
</head>
<body>
  <main class="card">
    <h1 class="person-name">Dale Whitmore</h1>
    <p class="person-role">Public &amp; Media Relations Consultant</p>

    <p class="contact-line line-phone">
      <svg width="24" height="30" viewBox="0 0 24 30" aria-hidden="true"><path d="M6 2 L10 2 L12 9 L9 11 Q11 18 15 21 L18 18 L23 22 L21 27 Q15 29 8 20 Q2 11 6 2 Z" fill="var(--brand-blue)"/></svg>
      317 555 0142
    </p>
    <p class="contact-line line-mobile">
      <svg width="24" height="34" viewBox="0 0 24 34" aria-hidden="true"><rect x="3" y="2" width="18" height="30" rx="3" fill="none" stroke="var(--brand-blue)" stroke-width="2.5"/><line x1="3" y1="26" x2="21" y2="26" stroke="var(--brand-blue)" stroke-width="2"/><circle cx="12" cy="29" r="1.2" fill="var(--brand-blue)"/></svg>
      317 555 0187
    </p>
    <p class="contact-line line-email">
      <svg width="32" height="22" viewBox="0 0 32 22" aria-hidden="true"><rect x="2" y="2" width="28" height="18" fill="none" stroke="var(--brand-blue)" stroke-width="2.2"/><path d="M2 2 L16 13 L30 2" fill="none" stroke="var(--brand-blue)" stroke-width="2.2"/></svg>
      dwhitmore44@mailbox.net
    </p>
    <p class="contact-line line-address">
      <svg width="32" height="28" viewBox="0 0 32 28" aria-hidden="true"><path d="M16 2 L31 11 L1 11 Z" fill="var(--brand-blue)"/><rect x="4" y="13" width="24" height="14" fill="var(--brand-blue)"/><rect x="13" y="17" width="6" height="10" fill="var(--white)"/></svg>
      2718 Larkspur Lane Indianapolis,
    </p>
    <p class="address-city">IN 46237</p>

    <div class="brand-mark-area" role="img" aria-label="Space for the company's brand symbol"></div>

    <svg class="footer-band" viewBox="0 0 660 240" aria-hidden="true">
      <defs>
        <linearGradient id="silverArc" x1="0" x2="1" y1="0" y2="0">
          <stop offset="0" stop-color="#8e9195"/>
          <stop offset="0.5" stop-color="#f4f4f5"/>
          <stop offset="1" stop-color="#8e9195"/>
        </linearGradient>
        <linearGradient id="blueBand" x1="0" x2="0" y1="0" y2="1">
          <stop offset="0" stop-color="var(--bright-blue)"/>
          <stop offset="0.55" stop-color="var(--brand-blue)"/>
          <stop offset="1" stop-color="var(--deep-blue)"/>
        </linearGradient>
      </defs>
      <path d="M0 50 Q330 -18 660 50 L660 240 L0 240 Z" fill="url(#silverArc)"/>
      <path d="M0 72 Q330 8 660 72 L660 240 L0 240 Z" fill="url(#blueBand)"/>
    </svg>
    <p class="company-name">Whitmore Communications</p>
  </main>
</body>
</html>
```